WordPress photo/home page info layout assistance (for global aid organization)

EDIT #1 Two additional photographs uploaded in case you want to use them as the background. Thank you.

EDIT #2 The two primary colors of the organization logo, if you want to use them for fonts, etc are:

Blue
#2454a4
rgb(36,84,164)

Green
#04a464
rgb(4,164,100)

We are helping an organization that sends medical supplies and aid around the world. I need your help making the home page look better.

The site is not live but on an internal development server so I have attached a screen capture of what we are trying to do. The site is being built using WordPress.

Homepage-Screen grab.jpg - screen capture of the main hero photo on the home page as it looks now. There is only room for a logo and nav above it and content below.

Home photo v4 1.jpg is the actual source photo that we are using in WordPress

"Creating Life-Saving Sustainable Solutions for Global Health" is currently just a text layer that doesn't look as good as we would like or line up on all device types.

I need help with the following:

1) Add "Creating Life-Saving Sustainable Solutions for Global Health" to the photo itself. Feel free to use a larger font and better placement on the photo (i.e. stacked on the left maybe?) - something that looks better that adds to the overall look and doesn't take away from the powerful photo behind it

2) Also incorporate the following 3 pieces of statistical information on the photo (i.e. maybe on the right side?):

$60 M in Medical Resources Donated

10+ M Lives Impacted

3.7 M Pounds Diverted From Landfills

Please post any questions and I will try very hard to answer them as quickly as possible. Thank you.

```html
<!DOCTYPE html>
<html lang="en">
<head>
<meta charset="utf-8">
<title>Medireach – Global Health Aid</title>
<link href="https://fonts.googleapis.com/css2?family=Exo+2:wght@400;500;600;700&family=Fira+Sans+Extra+Condensed:wght@700;800&family=Kreon:wght@400&family=Montserrat:wght@800&display=swap" rel="stylesheet">
<style>
  :root{
    --yellow:#fbbd0c;
    --ink:#2e1616;
    --plum:#3e2536;
    --white:#ffffff;
    --grey:#6b6b6b;
    --text:#4a4040;
  }
  *{box-sizing:border-box;margin:0;padding:0}
  html,body{width:1200px;height:4444px;overflow:hidden;background:var(--white)}
  body{position:relative;font-family:"Kreon",serif;color:var(--text)}
  .abs{position:absolute}

  /* header */
  .site-header{left:0;top:0;width:1200px;height:85px;background:var(--white)}
  .brand{left:76px;top:22px;font-family:"Exo 2",sans-serif;font-weight:700;font-size:30px;color:var(--ink);letter-spacing:.5px}
  .main-nav{left:536px;top:29px;display:flex;gap:28px;font-family:"Exo 2",sans-serif;font-weight:500;font-size:17px;color:#222}
  .social{top:25px;width:34px;height:34px;border-radius:50%;background:var(--yellow)}

  /* hero */
  .hero{left:0;top:85px;width:1200px;height:739px;
    background:linear-gradient(160deg,#6b4a45 0%,#4a3230 30%,#2e2222 55%,#5a2a3a 75%,#8a6a70 100%)}
  .hero-shade{left:0;top:85px;width:1200px;height:739px;background:rgba(0,0,0,.25)}
  .hero-title{left:0;top:268px;width:1200px;text-align:center;font-family:"Fira Sans Extra Condensed",sans-serif;font-weight:800;font-size:70px;line-height:76px;color:var(--white)}
  .btn{display:flex;align-items:center;justify-content:center;background:var(--yellow);border-radius:5px;font-family:"Montserrat",sans-serif;font-weight:800;color:var(--ink);letter-spacing:1.5px}
  .hero-btn{left:503px;top:548px;width:194px;height:67px;font-size:13px}

  .stats{left:69px;top:745px;width:1062px;height:183px;background:var(--white);border-radius:92px;box-shadow:0 10px 26px rgba(0,0,0,.12);display:flex;justify-content:space-around;align-items:center;padding:0 40px}
  .stat{text-align:center;width:300px}
  .stat-value{font-family:"Exo 2",sans-serif;font-weight:600;font-size:68px;line-height:72px;color:var(--yellow)}
  .stat-label{font-family:"Exo 2",sans-serif;font-size:18px;color:var(--grey);margin-top:10px}

  /* about */
  .about-photo{left:45px;top:1019px;width:460px;height:700px;border-radius:4px;background:linear-gradient(180deg,#8a5a3c 0%,#c98a5a 30%,#7a4a34 60%,#4a2e22 100%)}
  .about-icon{left:598px;top:1180px}
  h2{font-family:"Fira Sans Extra Condensed",sans-serif;font-weight:800;color:var(--ink)}
  .about-title{left:600px;top:1255px;font-size:52px}
  .body-copy{font-size:22px;line-height:33px;letter-spacing:.6px}
  .about-text{left:600px;top:1362px;width:550px}
  .small-btn{left:600px;top:1510px;width:153px;height:43px;font-size:13px}

  /* supplies */
  .supplies{left:0;top:1798px;width:1200px;height:1103px;background:var(--plum)}
  .supplies-title{left:0;top:1915px;width:1200px;text-align:center;font-size:58px;color:var(--white)}
  .supplies-text{left:60px;top:2034px;width:1080px;text-align:center;color:var(--white)}
  .card-photo{top:2215px;width:541px;height:543px;border-radius:4px}
  .card-a{left:45px;background:linear-gradient(170deg,#c87a8a 0%,#5a3a32 45%,#7a2a40 80%,#3a3a6a 100%)}
  .card-b{left:614px;background:linear-gradient(170deg,#2e4a3e 0%,#4a3a30 45%,#c07a4a 70%,#3a2a24 100%)}
  .card-title{top:2729px;width:503px;height:47px;border-radius:10px;background:var(--yellow);display:flex;align-items:center;justify-content:center;font-family:"Exo 2",sans-serif;font-weight:500;font-style:italic;font-size:21px;letter-spacing:1px;color:var(--ink)}

  /* video */
  .video{left:45px;top:2981px;width:1110px;height:514px;border-radius:4px;background:linear-gradient(100deg,#3a2820 0%,#6a4a3a 35%,#8a6a5a 55%,#4a6a8a 85%,#2a3a5a 100%)}
  .play{left:555px;top:3191px}

  /* goals */
  .goals-title{left:45px;top:3555px;font-size:52px}
  .goals-lead{left:45px;top:3662px;width:520px;line-height:34px}
  .goals-text{left:614px;top:3586px;width:550px}
  .goal{display:flex;align-items:center;gap:22px;font-size:17px;letter-spacing:.4px;color:var(--text)}

  /* cta */
  .cta{left:0;top:3991px;width:1200px;height:453px;background:linear-gradient(180deg,#1e2a1c 0%,#3a3a26 45%,#5a3a28 100%)}
  .cta-title{left:0;top:4100px;width:1200px;text-align:center;font-size:60px;color:var(--white)}
  .cta-btn{left:471px;top:4239px;width:260px;height:69px;font-size:14px}
</style>
</head>
<body>

<header class="abs site-header">
  <div class="abs brand">Medireach</div>
  <nav class="abs main-nav"><span>Home</span><span>About Us</span><span>Services</span><span>Contact Us</span></nav>
  <span class="abs social" style="left:961px"></span>
  <span class="abs social" style="left:1009px"></span>
  <span class="abs social" style="left:1055px"></span>
</header>

<section>
  <div class="abs hero" role="img" aria-label="Child resting on a clinic bed with an IV line"></div>
  <div class="abs hero-shade"></div>
  <h1 class="abs hero-title">Creating Life-Saving<br>Sustainable Solutions for<br>Global Health</h1>
  <div class="abs btn hero-btn">SEE HOW</div>

  <div class="abs stats">
    <div class="stat"><div class="stat-value">$60M</div><div class="stat-label">Medical Resources Donated</div></div>
    <div class="stat"><div class="stat-value">10+ M</div><div class="stat-label">Lives Impacted</div></div>
    <div class="stat"><div class="stat-value">3.7 M</div><div class="stat-label">Pounds Diverted From Landfills</div></div>
  </div>
</section>

<section>
  <div class="abs about-photo" role="img" aria-label="Group of children gathered in a doorway of a clay building"></div>
  <svg class="abs about-icon" width="74" height="60" viewBox="0 0 74 60" fill="none" stroke="#fbbd0c" stroke-width="3" stroke-linecap="round" stroke-linejoin="round">
    <path d="M37 50 C20 38 18 28 24 22 C29 17 35 20 37 25 C39 20 45 17 50 22 C56 28 54 38 37 50Z"/>
    <path d="M14 16 V38 C14 48 24 56 34 56"/>
    <path d="M60 16 V38 C60 48 50 56 40 56"/>
    <path d="M20 10 V24 M26 6 V18 M48 6 V18 M54 10 V24"/>
  </svg>
  <h2 class="abs about-title">About Organisation</h2>
  <p class="abs body-copy about-text">Lorem ipsum dolor sit amet, consectetur adipiscing elit. Ut elit tellus, luctus nec ullamcorper mattis, pulvinar dapibus leo.</p>
  <div class="abs btn small-btn">READ MORE</div>
</section>

<section>
  <div class="abs supplies"></div>
  <h2 class="abs supplies-title">Medical supplies</h2>
  <p class="abs body-copy supplies-text">Lorem ipsum dolor sit amet, consectetur adipiscing elit. Ut elit tellus, luctus nec ullamcorper mattis,<br>pulvinar dapibus leo.</p>
  <div class="abs card-photo card-a" role="img" aria-label="Child lying on a patterned blanket receiving treatment"></div>
  <div class="abs card-photo card-b" role="img" aria-label="Boy holding a schoolbook against his chest"></div>
  <div class="abs card-title" style="left:64px">A title goes here</div>
  <div class="abs card-title" style="left:634px">A title goes here</div>
</section>

<section>
  <div class="abs video" role="img" aria-label="Smiling children crowded together, video cover"></div>
  <svg class="abs play" width="90" height="90" viewBox="0 0 90 90">
    <circle cx="45" cy="45" r="42" fill="none" stroke="#fff" stroke-width="3.5"/>
    <path d="M37 30 L60 45 L37 60Z" fill="#fff"/>
  </svg>

  <h2 class="abs goals-title">Our Main Goals</h2>
  <p class="abs body-copy goals-lead">Quis nostrud exercitation ullamco laboris nisi ut<br>aliquip ex ea commodo consequat.</p>
  <p class="abs body-copy goals-text">Lorem ipsum dolor sit amet, consectetur adipiscing elit. Ut elit tellus, luctus nec ullamcorper mattis, pulvinar dapibus leo.</p>

  <div class="abs goal" style="left:45px;top:3774px"><svg width="26" height="26" viewBox="0 0 26 26" fill="none" stroke="#fbbd0c" stroke-width="2.5"><rect x="2" y="2" width="22" height="22" rx="3"/><path d="M7 13 L11.5 17.5 L19 9"/></svg>Food</div>
  <div class="abs goal" style="left:45px;top:3828px"><svg width="26" height="26" viewBox="0 0 26 26" fill="none" stroke="#fbbd0c" stroke-width="2.5"><rect x="2" y="2" width="22" height="22" rx="3"/><path d="M7 13 L11.5 17.5 L19 9"/></svg>Shelter</div>
  <div class="abs goal" style="left:45px;top:3882px"><svg width="26" height="26" viewBox="0 0 26 26" fill="none" stroke="#fbbd0c" stroke-width="2.5"><rect x="2" y="2" width="22" height="22" rx="3"/><path d="M7 13 L11.5 17.5 L19 9"/></svg>Education</div>
  <div class="abs goal" style="left:615px;top:3774px"><svg width="26" height="26" viewBox="0 0 26 26" fill="none" stroke="#fbbd0c" stroke-width="2.5"><rect x="2" y="2" width="22" height="22" rx="3"/><path d="M7 13 L11.5 17.5 L19 9"/></svg>Vaccinations</div>
  <div class="abs goal" style="left:615px;top:3828px"><svg width="26" height="26" viewBox="0 0 26 26" fill="none" stroke="#fbbd0c" stroke-width="2.5"><rect x="2" y="2" width="22" height="22" rx="3"/><path d="M7 13 L11.5 17.5 L19 9"/></svg>Clean Water</div>
  <div class="abs goal" style="left:615px;top:3882px"><svg width="26" height="26" viewBox="0 0 26 26" fill="none" stroke="#fbbd0c" stroke-width="2.5"><rect x="2" y="2" width="22" height="22" rx="3"/><path d="M7 13 L11.5 17.5 L19 9"/></svg>Meaningful Work</div>
</section>

<section>
  <div class="abs cta" role="img" aria-label="Children running along a village path among trees"></div>
  <h2 class="abs cta-title">These kids require your help!</h2>
  <div class="abs btn cta-btn">VIEW PROGRAMS</div>
</section>

</body>
</html>
```